Moder Business Card Design for Renewables Business

Need a business card design for my business. We collect & repurpose spent coffee ground from cafes. The cards will be made from recycled paper. Needs to fit our corporate colour scheme of white, green & brown (see logo for colour codes). Eco friendly, modern, intresting & eye catching.
This card needs to convey the message of the business and fit into its mantra of eco-friendly, sustainable etc.

Target Market(s)

Cafe Owners, Coffee Drinkers, Recycling Companies, Farmers

Industry/Entity Type

Recycling

Contact Information for Business Card

Name; Peter Halloran
Phone; 0412 386 527
e-mail; info@lumatrove.com.au
website; www.lumatrove.com.au

Font styles to use
Sans Serif
Script

Colors

Designer to choose colors to be used in the design.

Requirements
Must have
• FRONT;
• Logo, Name (Peter Halloran), phone number, e-mail address, website
• BACK;
• On the back in cursive text; 'SUSTAINABILITY IN THE DAILY GRIND'
• Small facebook & Instagram logos with text 'Lumatrove'
Should not have
• messy design

```html
<!DOCTYPE html>
<html lang="en">
<head>
<meta charset="UTF-8">
<title>Lumatrove – Business Card Back</title>
<link rel="stylesheet" href="https://fonts.googleapis.com/css2?family=Lobster&family=Lexend:wght@400&display=block">
<style>
  :root {
    --coffee-brown: #612f16;
    --leaf-green: #7aa640;
    --paper-white: #ffffff;
  }
  html, body {
    margin: 0;
    padding: 0;
    width: 1200px;
    height: 686px;
    overflow: hidden;
    background: var(--paper-white);
  }
  .card {
    position: relative;
    width: 1200px;
    height: 686px;
    border-radius: 46px;
    overflow: hidden;
    background: var(--coffee-brown);
  }
  .tagline {
    position: absolute;
    left: 0;
    right: 0;
    top: 248px;
    margin: 0;
    text-align: center;
    font-family: "Lobster", "Brush Script MT", cursive;
    font-weight: 400;
    font-size: 62px;
    line-height: 1;
    letter-spacing: -0.5px;
    color: var(--leaf-green);
    white-space: nowrap;
  }
  .social-band {
    position: absolute;
    left: 0;
    right: 0;
    bottom: 0;
    height: 108px;
    background: var(--leaf-green);
  }
  .social-handle {
    position: absolute;
    top: 50%;
    transform: translateY(-50%);
    display: flex;
    align-items: center;
    gap: 5px;
    font-family: "Lexend", sans-serif;
    font-weight: 400;
    font-size: 24px;
    color: var(--coffee-brown);
    white-space: nowrap;
  }
  .social-handle--left { left: 68px; }
  .social-handle--right { left: 918px; }
  .social-dot {
    width: 55px;
    height: 55px;
    border-radius: 50%;
    background: var(--coffee-brown);
    flex: none;
  }
</style>
</head>
<body>
  <main class="card">
    <h1 class="tagline">Sustainability In The Daily Grind</h1>
    <footer class="social-band">
      <div class="social-handle social-handle--left">
        <span class="social-dot"></span>
        <span class="social-name">Lumatrove</span>
      </div>
      <div class="social-handle social-handle--right">
        <span class="social-dot"></span>
        <span class="social-name">Lumatrove</span>
      </div>
    </footer>
  </main>
</body>
</html>
```